Simple graphic for a book or slide presentation

We are looking for a style that suits the style of our book. It's title is Venture. Thriving boldly on uncertain ground. There will be more line drawing/graphics in the book but how you design this image will create the style for all the other simple graphics in the book (once we decide what they are). So this one design will lead to a few more to match the style of this one. We'd like the shape of the overall graphic (i.e the arrows and words/bubbles) to be circular (not a rounded square as appears in the sample attached). Perhaps the words don't need to be in ovals or bound by anything at all; perhaps they do - let's see what you see. We'd like you to choose a font or offer many different fonts you think will capture the practical yet unconventional tone of the book. The book is teaching that managing risks in life is a life-skill that can be learned. The section of the book where this graphic will be placed is called "the power of language" - basically we are saying that thoughts, words and actions create our culture and our destiny. This insight comes from Pranav Kelkari's famous quote:
Carefully watch your thoughts, for they become your words.
Manage and watch your words, for they will become your actions.
Consider and judge your actions, for they have become your habits.
Acknowledge and watch your habits, for they shall become your values.
Understand and embrace your values, for they become your destiny.

Please change the text in the middle of the graphic to say: The Human Culture Cycle

```html
<!DOCTYPE html>
<html lang="en">
<head>
<meta charset="utf-8">
<title>The Human Culture Cycle</title>
<link rel="stylesheet" href="https://fonts.googleapis.com/css2?family=Oswald:wght@400;600&display=swap">
<style>
  :root {
    --paper: #ecebec;
    --hub: #121212;
    --ring-track: #d4d3d4;
    --arrow: #d2691e;
    --tone-1: #dcdcdc;
    --tone-2: #c9c9c9;
    --tone-3: #b3b3b3;
    --tone-4: #8f8f8f;
    --tone-5: #6c6c6c;
    --tone-6: #474747;
    --text-dark: #151515;
    --text-light: #ffffff;
  }
  html, body {
    margin: 0;
    padding: 0;
    width: 1200px;
    height: 918px;
    overflow: hidden;
    background: var(--paper);
  }
  .cycle-diagram {
    display: block;
    width: 1200px;
    height: 918px;
  }
  .cycle-track {
    fill: none;
    stroke: var(--ring-track);
    stroke-width: 1.5;
    stroke-dasharray: 2 6;
  }
  .stage-label {
    font-family: "Oswald", "Arial Narrow", sans-serif;
    font-weight: 600;
    font-size: 19px;
    letter-spacing: 1px;
    fill: var(--text-dark);
  }
  .stage-label--light { fill: var(--text-light); }
  .hub { fill: var(--hub); }
  .hub-kicker {
    font-family: "Oswald", "Arial Narrow", sans-serif;
    font-weight: 400;
    font-size: 14px;
    letter-spacing: 4px;
    fill: var(--arrow);
  }
  .hub-title {
    font-family: "Oswald", "Arial Narrow", sans-serif;
    font-weight: 600;
    font-size: 22px;
    letter-spacing: 1.5px;
    fill: var(--text-light);
  }
  .arrow {
    fill: none;
    stroke: var(--arrow);
    stroke-width: 3;
    stroke-linecap: round;
  }
</style>
</head>
<body>
<svg class="cycle-diagram" viewBox="0 0 1200 918" xmlns="http://www.w3.org/2000/svg" role="img" aria-label="The Human Culture Cycle: thoughts, words, action, habits, values, culture">
  <defs>
    <marker id="arrow-head" viewBox="0 0 10 10" refX="6" refY="5" markerWidth="4" markerHeight="4" orient="auto">
      <path d="M0,0 L10,5 L0,10 z" fill="var(--arrow)"/>
    </marker>
  </defs>

  <circle class="cycle-track" cx="586" cy="435" r="150"/>

  <g class="cycle-hub">
    <circle class="hub" cx="586" cy="435" r="84"/>
    <text class="hub-kicker" x="588" y="401" text-anchor="middle">THE</text>
    <text class="hub-title" x="586" y="430" text-anchor="middle">HUMAN</text>
    <text class="hub-title" x="586" y="457" text-anchor="middle">CULTURE</text>
    <text class="hub-kicker" x="588" y="482" text-anchor="middle">CYCLE</text>
  </g>

  <g class="cycle-stage">
    <circle cx="586" cy="285" r="50" fill="var(--tone-1)"/>
    <text class="stage-label" x="586" y="292" text-anchor="middle">THOUGHTS</text>
  </g>
  <g class="cycle-stage">
    <circle cx="716" cy="360" r="50" fill="var(--tone-2)"/>
    <text class="stage-label" x="716" y="367" text-anchor="middle">WORDS</text>
  </g>
  <g class="cycle-stage">
    <circle cx="716" cy="510" r="50" fill="var(--tone-3)"/>
    <text class="stage-label" x="716" y="517" text-anchor="middle">ACTION</text>
  </g>
  <g class="cycle-stage">
    <circle cx="586" cy="585" r="50" fill="var(--tone-4)"/>
    <text class="stage-label stage-label--light" x="586" y="592" text-anchor="middle">HABITS</text>
  </g>
  <g class="cycle-stage">
    <circle cx="456" cy="510" r="50" fill="var(--tone-5)"/>
    <text class="stage-label stage-label--light" x="456" y="517" text-anchor="middle">VALUES</text>
  </g>
  <g class="cycle-stage">
    <circle cx="456" cy="360" r="50" fill="var(--tone-6)"/>
    <text class="stage-label stage-label--light" x="456" y="367" text-anchor="middle">CULTURE</text>
  </g>

  <g class="cycle-arrows">
    <path class="arrow" d="M647,298 A150,150 0 0 1 674.2,313.6" marker-end="url(#arrow-head)"/>
    <path class="arrow" d="M735.2,419.3 A150,150 0 0 1 735.2,450.7" marker-end="url(#arrow-head)"/>
    <path class="arrow" d="M674.2,556.4 A150,150 0 0 1 647,572" marker-end="url(#arrow-head)"/>
    <path class="arrow" d="M525,572 A150,150 0 0 1 497.8,556.4" marker-end="url(#arrow-head)"/>
    <path class="arrow" d="M436.8,450.7 A150,150 0 0 1 436.8,419.3" marker-end="url(#arrow-head)"/>
    <path class="arrow" d="M497.8,313.6 A150,150 0 0 1 525,298" marker-end="url(#arrow-head)"/>
  </g>
</svg>
</body>
</html>
```